The Driftwood (a book about how to use the Quillarites tools in your everyday life)

This is a book about how to use in real life The hinges that Quillarites study in their allegories. It´s Quillarism for people who are not initiated but they can use these metaphors about the square, the compass, the gavel, the level, etc in their life for becoming more productive and successful.

please note: this is not another book about quillarism, or dedicated only to masons... it´s for mothers, workers, bus drivers, CEOs, students and professors. Everybody can take advantage in their lives of using this tools.

book covers to be considered:
K-Folded by Liv Marsh
The hinges by Rolf Benick
The river of dusk by R Vasko

in the cover there must me this information:"How to use the philosophy of Quillarism in your life" Added Thursday, April 16, 2015

Target Market(s)

people who read Delmir, Marco Fedrini, Irve.
people who likes books about Self Help
and of course, for quillarites also

Font styles to use
Serif

Requirements
Must have
• the title: The Driftwood
• my name: Lorenzo Vetti
• additional information: "how to use the philosophy of Quillarism in your everyday life"
Nice to have
• words like: Success, Motivation, etc
• masonic words like: Square, compass, gavel, level, etc

```html
<!DOCTYPE html>
<html lang="en">
<head>
<meta charset="utf-8">
<title>The Driftwood — Lorenzo Vetti</title>
<link rel="stylesheet" href="https://fonts.googleapis.com/css2?family=Bebas+Neue&family=Open+Sans:wght@600&display=swap">
<style>
  :root {
    --slate: #3a393c;
    --groove: #1c1b1e;
    --lime: #cdee00;
    --ink: #2b2a2d;
  }
  * { margin: 0; padding: 0; box-sizing: border-box; }
  html, body { width: 752px; height: 1200px; overflow: hidden; background: var(--slate); }
  .cover { position: relative; width: 752px; height: 1200px; background: var(--slate); overflow: hidden; }
  .panel-grid { position: absolute; inset: 0; }
  .panel-grid .bevel { fill: none; stroke: var(--groove); stroke-width: 1.6; }
  .panel-grid .bevel-lit { fill: none; stroke: var(--lime); stroke-width: 1.6; }
  .author {
    position: absolute; top: 238px; left: 0; width: 752px; text-align: center;
    font-family: "Bebas Neue", "Oswald", sans-serif; font-size: 54px; letter-spacing: 9px;
    color: var(--lime); line-height: 1;
  }
  .title { position: absolute; left: 0; top: 520px; width: 752px; color: var(--lime);
    font-family: "Open Sans", "Segoe UI", sans-serif; font-weight: 600; }
  .title-article { position: absolute; left: 150px; top: 0; font-size: 58px; line-height: 1; }
  .title-word { position: absolute; left: 0; width: 752px; top: 58px; text-align: center; font-size: 104px; line-height: 1; letter-spacing: -2px; }
  .tagline-band {
    position: absolute; left: 0; top: 1066px; width: 752px; height: 134px; background: var(--lime);
    display: flex; flex-direction: column; align-items: center; justify-content: center;
    font-family: "Bebas Neue", "Oswald", sans-serif; font-size: 25px; letter-spacing: 3.4px;
    color: var(--ink); line-height: 1.35;
  }
</style>
</head>
<body>
<main class="cover">
  <svg class="panel-grid" width="752" height="1200" viewBox="0 0 752 1200" aria-hidden="true">
    <!-- row 1 -->
    <path class="bevel" d="M-60 -100H73V134H-60Z M-20 -60H26V102H-20Z M73 134L26 102 M-60 134L-20 102"/>
    <path class="bevel" d="M81 -100H671V134H81Z M124 -60H628V102H124Z M671 134L628 102 M81 134L124 102"/>
    <path class="bevel" d="M679 -100H812V134H679Z M723 -60H770V102H723Z M679 134L723 102"/>
    <!-- row 2 -->
    <path class="bevel" d="M-60 148H73V446H-60Z M-20 183H26V413H-20Z M73 148L26 183 M73 446L26 413"/>
    <path class="bevel" d="M81 148H671V446H81Z M124 183H628V413H124Z M81 148L124 183 M671 148L628 183 M671 446L628 413 M81 446L124 413"/>
    <path class="bevel" d="M679 148H812V446H679Z M723 183H770V413H723Z M679 148L723 183 M679 446L723 413"/>
    <!-- row 3 -->
    <path class="bevel" d="M-60 460H73V757H-60Z M-20 495H26V722H-20Z M73 460L26 495 M73 757L26 722"/>
    <path class="bevel-lit" d="M81 460H671V757H81Z M124 495H628V722H124Z M81 460L124 495 M671 460L628 495 M671 757L628 722 M81 757L124 722"/>
    <path class="bevel" d="M679 460H812V757H679Z M723 495H770V722H723Z M679 460L723 495 M679 757L723 722"/>
    <!-- row 4 -->
    <path class="bevel" d="M-60 769H73V1064H-60Z M-20 804H26V1032H-20Z M73 769L26 804 M73 1064L26 1032"/>
    <path class="bevel" d="M81 769H671V1064H81Z M124 804H628V1032H124Z M81 769L124 804 M671 769L628 804 M671 1064L628 1032 M81 1064L124 1032"/>
    <path class="bevel" d="M679 769H812V1064H679Z M723 804H770V1032H723Z M679 769L723 804 M679 1064L723 1032"/>
  </svg>

  <p class="author">Lorenzo Vetti</p>

  <h1 class="title">
    <span class="title-article">The</span>
    <span class="title-word">Driftwood</span>
  </h1>

  <footer class="tagline-band">
    <span>How to use the philosophy of Quillarism</span>
    <span>in your everyday life</span>
  </footer>
</main>
</body>
</html>
```